Business Card Design

We recently had a new logo designed by Pixel Harbor. Now we want to create new business cards and letterhead that compliment our new logo.

We are audiologists in private practice specializing in hearing evaluations and fitting hearing aids. We want a clean and professional card.

We need business cards for each audiologist. The names and titles are:
Marnie Ostrova, AuD
Audiologist

Jen Tarbel, AuD
Audiologist

Corvina Plesk, AuD
Audiologist

We also need a business card with no provider. Just a generic one.

Finally, we need an appointment card. This is what the front desk uses to give to the patient with their next appointment date and time.

Target Market(s)

Our clients tend to be highly educated. They are older so the cards should be clean and easy to read. No squirrely font please.

Industry/Entity Type

Business

Contact Information for Business Card

20731 8th Ave NE, suite 417
Seattle, WA 98177
206-592-8074

Requirements
Must have
• Clean
Easy to read
Professional
Modern but approachable / warm
Should not have
• Other pictures besides the logo

```html
<!DOCTYPE html>
<html lang="en">
<head>
<meta charset="utf-8">
<title>Larkfield Hearing Services – Business Card</title>
<link rel="stylesheet" href="https://fonts.googleapis.com/css2?family=Open+Sans:wght@400;700&display=swap">
<style>
  :root {
    --backdrop: #e4e6ea;
    --card-white: #ffffff;
    --navy-deep: #283763;
    --navy-soft: #475178;
    --slate: #6c6f8f;
    --teal: #3aa58e;
    --ink: #1f2230;
    --muted: #4a4d5c;
  }
  * { margin: 0; padding: 0; box-sizing: border-box; }
  html, body {
    width: 1200px;
    height: 1000px;
    overflow: hidden;
    background: var(--backdrop);
    font-family: "Open Sans", Arial, sans-serif;
  }
  .business-card {
    position: absolute;
    left: 100px;
    top: 214px;
    width: 1000px;
    height: 572px;
    background: var(--card-white);
    overflow: hidden;
    box-shadow: 0 10px 30px rgba(30, 35, 60, 0.18);
  }
  .card-bands {
    position: absolute;
    inset: 0;
    width: 100%;
    height: 100%;
  }
  .brand-lockup {
    position: absolute;
    left: 190px;
    top: 58px;
    display: flex;
    align-items: center;
    gap: 18px;
  }
  .brand-dot {
    width: 74px;
    height: 74px;
    border-radius: 50%;
    background: var(--navy-deep);
    flex: none;
  }
  .brand-text { display: flex; flex-direction: column; }
  .brand-name {
    font-weight: 700;
    font-size: 30px;
    line-height: 1.1;
    color: var(--ink);
    letter-spacing: 0.5px;
    max-width: 330px;
  }
  .brand-tagline {
    margin-top: 6px;
    font-size: 17px;
    font-weight: 400;
    color: var(--muted);
    letter-spacing: 1px;
  }
  .contact-block {
    position: absolute;
    left: 0;
    right: 0;
    top: 330px;
    text-align: center;
    color: #ffffff;
    font-weight: 700;
  }
  .contact-phone {
    font-size: 30px;
    margin-left: 120px;
  }
  .contact-address {
    margin-top: 40px;
    font-size: 32px;
    margin-left: 60px;
  }
</style>
</head>
<body>
  <div class="business-card">
    <svg class="card-bands" viewBox="0 0 1000 572" preserveAspectRatio="none" aria-hidden="true">
      <defs>
        <linearGradient id="navy-panel" x1="0" y1="0" x2="0.3" y2="1">
          <stop offset="0" stop-color="#283763"/>
          <stop offset="1" stop-color="#475178"/>
        </linearGradient>
      </defs>
      <polygon class="band-slate" points="0,244 1000,112 1000,121 0,253" fill="var(--slate)"/>
      <polygon class="band-teal" points="0,255 1000,123 1000,131 0,263" fill="var(--teal)"/>
      <polygon class="panel-navy" points="0,263 1000,131 1000,572 0,572" fill="url(#navy-panel)"/>
    </svg>

    <div class="brand-lockup">
      <span class="brand-dot"></span>
      <div class="brand-text">
        <span class="brand-name">Larkfield Hearing Services</span>
        <span class="brand-tagline">We listen so you can hear</span>
      </div>
    </div>

    <div class="contact-block">
      <p class="contact-phone">Phone : 206-592-8074</p>
      <p class="contact-address">20731 8th Ave NE, suite 417 Seattle, WA 98177</p>
    </div>
  </div>
</body>
</html>
```